Emergency Management Consulting Needs a Website

Need to develop a website for an Emergency Management Consulting business. This website needs to be user friendly and resemble disaster preparedness, response, recovery, and mitigation. It must allow for me to make changes to it myself by adding pages, content and pictures. Looking for an advanced page to the website that allows monitoring of social media sites, hashtags, and keywords. Must have pictures of disasters on the site. Must try to integrate the logo colors, not excessive.

Reason: Did not receive anything sufficient to what I am looking for.

Industry/Entity Type

Government

Coding

Coded - Design and coding required

Number of Pages Required

5+ page

Requirements
Must have
• Logo, advanced social media monitoring page, allow for edits myself (content, pages, graphics) this must be a CMS of some sort, use logo color scheme (not excessively), must be professional looking, connect with Vexlo Domain, find a hosting site, SEO, no "long" designs, minimize "dead" space, no social media feeds, no newsletter stuff.
• Menu items: Home, About Us, Services, Situation Monitor, Work With Us, Contact Us (hopefully these could be editable if I need to later)
• When you make a submission, please send me a message on which CMS you are using. Thank you.
Nice to have
• Examples of websites:
• https://www.plorn.vic.gov.au/
• http://www.garvelmunds.com/
• http://www.tqplaxr.org/
• http://dumbrellconsulting.com/
• http://www.folvantix.com/services/emergency-management
• https://qzu.com/
• http://www.belmorvia.com/Responsibility/Sustainable-Development/HSE/Crisis-and-Emergency-Management/

```html
<!DOCTYPE html>
<html lang="en">
<head>
<meta charset="utf-8">
<title>Twin Fork Emergency Management</title>
<link href="https://fonts.googleapis.com/css2?family=Lato:wght@400;700&display=swap" rel="stylesheet">
<style>
  :root {
    --ink: #111111;
    --accent-orange: #f5a01a;
    --heading-orange: #e4602b;
    --link-blue: #1f72bd;
    --footer-bg: #161616;
    --white: #ffffff;
    --rule: #e6e6e6;
  }
  * { margin: 0; padding: 0; box-sizing: border-box; }
  html, body { width: 1200px; height: 946px; overflow: hidden; background: var(--white); }
  body { font-family: 'Lato', sans-serif; color: var(--ink); position: relative; }

  .site-header { position: absolute; top: 0; left: 0; width: 1200px; height: 73px; border-bottom: 1px solid var(--rule); }
  .brand { position: absolute; left: 124px; top: 20px; display: flex; align-items: center; gap: 8px; }
  .brand-mark { width: 30px; height: 30px; border-radius: 50%; background: var(--accent-orange); }
  .brand-name { font-size: 19px; font-weight: 700; color: #2b2b2b; letter-spacing: 0.5px; }
  .main-nav { position: absolute; right: 120px; top: 28px; display: flex; gap: 23px; }
  .main-nav a { font-size: 14px; letter-spacing: 0.8px; color: var(--ink); text-decoration: none; text-transform: uppercase; }
  .main-nav a.is-current { color: #2e9be0; }

  .hero { position: absolute; top: 73px; left: 0; width: 1200px; height: 385px;
    background: linear-gradient(160deg, #8e9a8a 0%, #b9bdb8 30%, #a7aca6 55%, #7f8d74 80%, #9aa294 100%); }
  .hero-panel { position: absolute; left: 112px; top: 0; width: 448px; height: 206px; background: rgba(80,80,80,0.72); }
  .hero-label { position: absolute; left: 40px; top: 42px; width: 338px; height: 35px; background: var(--accent-orange);
    color: var(--white); font-size: 19.5px; line-height: 35px; padding-left: 13px; }
  .hero-title { position: absolute; left: 38px; top: 92px; color: var(--white); font-size: 24px; font-weight: 400; }
  .hero-quote { position: absolute; left: 39px; top: 148px; color: var(--white); font-size: 13.5px; line-height: 25px; }

  .intro { position: absolute; top: 528px; width: 460px; }
  .intro-left { left: 120px; }
  .intro-right { left: 626px; width: 454px; }
  .section-title { color: var(--heading-orange); font-size: 20.5px; font-weight: 700; letter-spacing: 0.4px; }
  .section-sub { margin-top: 22px; color: var(--link-blue); font-size: 17px; font-weight: 700; letter-spacing: 0.4px; }
  .section-text { margin-top: 20px; font-size: 15.5px; line-height: 30.5px; }
  .intro-right .section-text { margin-top: 21px; }
  .more-link { display: flex; align-items: center; gap: 18px; color: var(--link-blue); font-size: 14px; font-weight: 700;
    letter-spacing: 0.6px; text-decoration: none; margin-top: 30px; }
  .case-photo { margin-top: 20px; width: 453px; height: 127px;
    background: linear-gradient(100deg, #6b5a48 0%, #9a8d7d 35%, #7c8aa0 60%, #a39580 100%); }
  .intro-right .more-link { margin-top: 26px; }

  .site-footer { position: absolute; left: 0; top: 888px; width: 1200px; height: 58px; background: var(--footer-bg);
    color: var(--white); font-size: 10px; text-align: center; line-height: 58px; }
</style>
</head>
<body>
  <header class="site-header">
    <div class="brand">
      <span class="brand-mark"></span>
      <span class="brand-name">TWIN FORK</span>
    </div>
    <nav class="main-nav">
      <a href="#" class="is-current">Home</a>
      <a href="#">About Us</a>
      <a href="#">Services</a>
      <a href="#">Situation Monitor</a>
      <a href="#">Work With Us</a>
      <a href="#">Contact Us</a>
    </nav>
  </header>

  <section class="hero" role="img" aria-label="Aerial photograph of a flooded village with houses and trees standing in water">
    <div class="hero-panel">
      <div class="hero-label">Twin Fork Emergency Management</div>
      <h1 class="hero-title">We help clients prepare for disasters.</h1>
      <p class="hero-quote">“It wasn't raining when Noah built the ark”<br>-- Harlan Voss --</p>
    </div>
  </section>

  <section class="intro intro-left">
    <h2 class="section-title">Welcome to</h2>
    <h3 class="section-sub">Twin Fork Emergency Management Consulting</h3>
    <p class="section-text">Lorem ipsum dolor sit amet, consectetur adipiscing elit. Maecenas eleifend risus ex, quis laoreet nisl vestibulum sed. Maecenas rutrum venenatis nibh a posuere. Quisque lacinia nulla ac turpis luctus varius.</p>
    <a class="more-link" href="#">
      <svg width="22" height="12" viewBox="0 0 22 12" aria-hidden="true"><path d="M1 6h19M15 1l5 5-5 5" fill="none" stroke="currentColor" stroke-width="1.8"/></svg>
      Read more About Us
    </a>
  </section>

  <section class="intro intro-right">
    <h2 class="section-title">Case Studies</h2>
    <p class="section-text">We strive to make a difference in people's lives.</p>
    <div class="case-photo" role="img" aria-label="Photograph of two relief workers walking through storm debris"></div>
    <a class="more-link" href="#">
      <svg width="22" height="12" viewBox="0 0 22 12" aria-hidden="true"><path d="M1 6h19M15 1l5 5-5 5" fill="none" stroke="currentColor" stroke-width="1.8"/></svg>
      Read more About Our Case Studies
    </a>
  </section>

  <footer class="site-footer">Copyright © 2017 TWIN FORK EMERGENCY MANAGEMENT</footer>
</body>
</html>
```